BRVL Brochure Design

Northfield Council of Clinical Standards (BRVL) needs a whole new brochure. I've upload EPS logos and past brochures. Our tagline is to "modernize healthcare" and we think our brochure should reflect that, so that's the purpose of this project.

BRVL is a proven leader in healthcare education, training and
consulting services for health professionals. We’ve earned a reputation for excellence in healthcare quality improvement and management.

BRVL works to improve healthcare quality by educating healthcare professionals about healthcare best practices. We focus on instructing our clients on how to plan for, measure, and improve healthcare quality in all facilities and facets such as:

Patient Safety
Infection Control
Performance Improvement
Risk Management
Compliance and Accreditation
Health and Hospital Administration
Health Insurance
Healthcare Financial Management
Facility Management and Safety

DESIGN SUGGESTIONS:

Brochure Size: 8.5 X 11 full size brochure or 8.5 X 11 trifold brochure

Number of Pages: 2 to 3

Colors: Feel free to use a wide array of colors but try to stay away from colors that are too loud, ex: Pink, Purple, Neon Green.

Themes: Professional, Educational

Designs:

Pelor by Oskar Lindqvist

Quorvo Pamphlet by Derek Malloway

Lanterns for harvest by Solvendri

Paisaje de Sr KT by vrpl

http://www.plimbask.com/post/28461937205/10-creative-brochure-designs

Don't limit yourself to these examples. However, these are examples we liked

Reason: We would like to see more designs

We want more full page designs than tri-fold 

We are considering both tri-fold and full-page but would like to see more full page designs 

Reason: Our lead designer making the decisions on this project has been fired. I apologize for the inconvenience. We want extend the project one last time

Target Market(s)

Students, Doctors, and Educational Professionals

Industry/Entity Type

Healthcare

Logo Text

asdfasdf

Font styles to use
Serif
Sans Serif
Decorative
Script

Requirements
Should not have
• Pink, Purple, Neon Green colors

```html
<!DOCTYPE html>
<html lang="en">
<head>
<meta charset="utf-8">
<title>BRVL Certificate Programs</title>
<link href="https://fonts.googleapis.com/css2?family=Oswald:wght@500&family=PT+Serif:wght@700&display=swap" rel="stylesheet">
<style>
  :root {
    --heading: #1e3a5f;
    --body: #2a2a2a;
    --panel: rgba(255,255,255,0.86);
    --divider: #8c9aab;
    --photo-light: #e6eaee;
    --photo-mid: #c4cdd6;
    --photo-warm: #d8c8bc;
  }
  html, body { margin: 0; padding: 0; overflow: hidden; }
  .page {
    position: relative;
    width: 927px;
    height: 1200px;
    overflow: hidden;
    background: var(--photo-light);
  }
  .page-photo {
    position: absolute; inset: 0;
    background:
      radial-gradient(ellipse at 20% 30%, var(--photo-warm) 0%, transparent 45%),
      radial-gradient(ellipse at 75% 55%, var(--photo-mid) 0%, transparent 50%),
      radial-gradient(ellipse at 40% 85%, var(--photo-mid) 0%, transparent 55%),
      linear-gradient(180deg, #f1f3f5 0%, #dfe4e9 50%, #eef0f2 100%);
  }
  .program-row {
    position: absolute;
    left: 38px;
    width: 872px;
    display: grid;
    grid-template-columns: 412px 460px;
    background: var(--panel);
  }
  .program { padding: 10px 14px 10px 12px; }
  .program + .program { border-left: 2px solid var(--divider); padding-left: 14px; }
  .program-title {
    font-family: "Oswald", sans-serif;
    font-weight: 500;
    font-size: 20px;
    letter-spacing: 0.2px;
    color: var(--heading);
    text-transform: uppercase;
    margin: 0 0 8px;
    line-height: 1.2;
    white-space: nowrap;
  }
  .program-title--long { font-size: 16.5px; letter-spacing: -0.2px; line-height: 24px; }
  .program-text {
    font-family: "PT Serif", serif;
    font-weight: 700;
    font-size: 11px;
    line-height: 16.6px;
    color: var(--body);
    margin: 0;
  }
</style>
</head>
<body>
<div class="page">
  <div class="page-photo" role="img" aria-label="Soft, faded photograph of healthcare professionals at work"></div>

  <section class="program-row" style="top:52px;height:268px">
    <article class="program">
      <h2 class="program-title">Certificate in Healthcare Quality</h2>
      <p class="program-text">The CHQ course is designed to give an in-depth but more generalized understanding of healthcare quality and its implementation. This course takes you through an overview of the healthcare systems in the US and a comparative study of other systems around the world, the concept of and principles of healthcare quality, and a history of how Quality has become an integral part of evaluating our healthcare system. Participants will hone their skills in organizational development, healthcare quality management, team building, problem solving techniques, and process improvement. By the end of this course, you will have learned how to assess, measure, and plan for, and improve quality within your healthcare organization.</p>
    </article>
    <article class="program">
      <h2 class="program-title">Certified Professional in Infection Control</h2>
      <p class="program-text">The CPIC course is designed to provide healthcare professionals with or without a background in epidemiology or microbiology, with a solid foundation of infection control practices. This course takes you through the basics of microbiology, epidemiology, patient and workplace safety, and infection control practices in a healthcare setting. By the end of the course, you will have learned local infection control standards, how to develop a team approach to infection control, and you will have designed a basic program for infection control in a healthcare facility.</p>
    </article>
  </section>

  <section class="program-row" style="top:344px;height:290px">
    <article class="program">
      <h2 class="program-title program-title--long">Certificate in Healthcare Risk Management</h2>
      <p class="program-text">The CHRM course is designed to help the healthcare professional identify and manage sources of risk as they occur in the healthcare setting. This course will cover the basics of risk management to ethical and legal issues associated with risks in the health environment. By the end of the course you will have acquired the skills you need to use, maintain, and extend the functionality of a risk management system by effectively using enterprise wide risk management tools and measures. You'll become aware of U.S. and international regulatory requirements concerning effective risk management and master the skills needed to acquire data from disparate data sources, configure your risk environment, develop appropriate risk factor models, perform risk analysis, and create results-oriented reports.</p>
    </article>
    <article class="program">
      <h2 class="program-title program-title--long">Certificate in Healthcare Performance Improvement</h2>
      <p class="program-text">The CHPI course is designed to enhance the healthcare professional's ability to implement healthcare quality policies and initiatives as well as the ability to quantify, measure, and secure results. This course takes you through an overview of healthcare quality including current, past, and local issues in performance measurement and improvement. Several of the quality tools will be practiced including FMEA, Six Sigma, FOCUS-PDCA, RCA, etc. Basic statistics methods and principles will also be presented. By the end of this course, you will be able to apply common performance improvement models and tools and develop a performance improvement plan.</p>
    </article>
  </section>

  <section class="program-row" style="top:644px;height:268px">
    <article class="program">
      <h2 class="program-title">Certificate in Hospital Surveying</h2>
      <p class="program-text">The CHS course is designed for individuals who take an interest in their hospital's accreditation process or who are involved in maintaining compliance for their healthcare facility. This course will take you through the survey process for The Clinical Accord Board, The Clinical Accord Board International and several other survey processes such as state licensure surveys, state and federal complaint surveys, Federal Medicare certification surveys, post-survey revisit surveys, and Life safety code surveys. This course also aims to guide you through the preparation of your facility for an unannounced survey. By the end of the course, you will understand how to assess your facility's survey readiness, how to perform a hospital survey, as well as how to effectively respond to survey findings.</p>
    </article>
    <article class="program">
      <h2 class="program-title program-title--long">Certificate in Health and Hospital Administration</h2>
      <p class="program-text">The CPHHA course is designed to give healthcare professionals more in depth coverage of the skills to manage and administer their hospitals as well as prepare healthcare administrators and executives for overseeing administrative programs and improvement projects. This course exposes participants to the complex organization of hospitals, internal operations, processes, roles, management techniques, information needs and technology utilization in the different components of the hospital system. By the end of the course you will have learned how to develop, implement, and evaluate a strategic plan for a healthcare facility, and you will have gained advanced skills for organizational success, leadership, and effectiveness and efficiency techniques.</p>
    </article>
  </section>

  <section class="program-row" style="top:928px;height:250px">
    <article class="program">
      <h2 class="program-title">Certified Patient Safety Officer</h2>
      <p class="program-text">The CPSO course is designed to help develop professional or research skills for those who are interested in effecting patient safety outcomes. This course will assist participants in understanding how to effectively meet the requirements of a patient safety program and how to implement national and international patient safety goals in healthcare organizations and in particular hospitals. Emphasis will be placed on the effective use of resources by developing intervention strategies based on patient and clinical risks. By the end of the course, you will have developed your own comprehensive patient safety program for your department, unit, or institution.</p>
    </article>
    <article class="program">
      <h2 class="program-title">Certified Professional in Infection Control</h2>
      <p class="program-text">The Fellowship program at the Northfield Council of Clinical Standards is designed to distinguish highly accomplished individuals working towards greater quality in healthcare. Fellows are accepted to the institute based upon our board's review of their qualifications, work experience, and knowledge of healthcare quality subjects. The FBRVL is a resource that fellowship candidates may utilize to help prepare for the fellowship exam.</p>
    </article>
  </section>
</div>
</body>
</html>
```